Responsive Website Design for New Social Site (Building User Account)

Brellomar.com is a website that allows people to create preformatted emails to be sent out at a later date. The purpose is to allow people to communicate in the event of an accident or death. The beta site is built but not consumable by the public. It needs a new look before we go live.

I’m speaking specifically about the user account. They are admin tools for creating and publishing communications. They include workflow design, document/message storage, and a dashboard.

I currently have a basic design. Now I’m looking for an inspired design. Something interesting and memorable. Something that draws people in. I have a PPT that can provide guidance on what elements need to be on each page but I’m looking for someone who knows how to create engaging websites.

SCOPE OF EFFORT
There are approximately 23 pages to the website but only 5 distinct page appearances
• Dashboard
• Workflow
• Document/Message/Contact Management
• Education Search
• Account Form
I need a few pop-up designs
• Yes/No/Continue
I need a responsive design (3 sizes)

ARTISTIC QUALITIES
Easy to Use/Understand
New/Inventive/Cool/Memorable
Works with the Logo
Consistent Elements (buttons, text, use of color, etc)

TECHNICAL ASPECTS
I’d like the work provided in a storyboard and individual files for development

PHASES
1. Initial Concept
a. 2-3 Designs Ideas. Just the Dashboard and Workflow in responsive formats
2. Build
a. Create all the pages
b. Provide in storyboard in responsive formats
c. 2 Rounds of Revision
3. Final
a. Provide Storyboard and Files

I'd like to see a portfolio of your responsive web design, especially any user accounts you have created. I've attached three of the initial pages. I'd like to see a concept of what you would produce for at least one of the pages.

Thank you for your interest.

```html
<!DOCTYPE html>
<html lang="en">
<head>
<meta charset="utf-8">
<title>Brellomar – Dashboard</title>
<link rel="stylesheet" href="https://fonts.googleapis.com/css2?family=Open+Sans:wght@400;600;700&display=swap">
<style>
:root{
  --page:#f3f3f3;
  --blue:#0e5ea8;
  --navy:#0a3f6c;
  --deep:#123a5c;
  --orange:#f47920;
  --green:#6db33f;
  --charcoal:#3e3e40;
  --ink:#3a3a3a;
  --row:#dedede;
  --white:#ffffff;
}
*{box-sizing:border-box;margin:0;padding:0}
html,body{width:1200px;height:936px;overflow:hidden;background:var(--page);font-family:"Open Sans",Arial,sans-serif;color:var(--ink)}
.frame{position:relative;width:1200px;height:936px;border-top:3px solid var(--navy)}
.sidebar{position:absolute;left:86px;top:0;width:204px;height:888px;background:var(--blue)}
.user{height:88px;display:flex;align-items:center;padding-left:18px;gap:9px;color:var(--white)}
.user svg{flex:none}
.user-name{font-weight:700;font-size:16px;line-height:20px}
.user-links{font-size:12px;line-height:16px}
.nav{list-style:none}
.nav li{height:40px;background:var(--orange);border-bottom:2px solid #f68b3d;display:flex;align-items:center;padding-left:17px;gap:7px;font-size:16px;color:#243347}
.nav svg{flex:none}
.main{position:absolute;left:314px;top:0;width:801px}
.brand{position:absolute;left:0;top:12px;display:flex;align-items:center;gap:10px}
.brand-dot{width:44px;height:44px;border-radius:50%;background:var(--orange)}
.brand-name{font-size:38px;font-weight:700;color:var(--blue);line-height:44px}
.tagline{position:absolute;left:70px;top:54px;font-size:11px;font-weight:600;color:#555;white-space:nowrap}
.account-links{position:absolute;right:0;top:34px;font-size:14px;color:var(--deep)}
.account-links span{margin:0 10px;color:#777}
.banner{position:absolute;left:0;top:90px;width:799px;height:140px;background:linear-gradient(90deg,#e4e2df,#f2f0ee 50%,#e2dfdb);border:3px solid #fff}
.banner-text{position:absolute;left:0;top:90px;width:799px;height:140px;text-align:center;padding-top:28px}
.banner-title{font-size:35px;font-weight:700;color:var(--orange);line-height:38px}
.banner-sub{font-size:29px;font-weight:700;color:var(--blue);line-height:36px}
.stats{position:absolute;top:266px;left:0;width:801px;height:112px}
.stat{position:absolute;top:0;width:182px;height:112px;padding:7px}
.stat div{width:100%;height:100%;border:1px solid rgba(255,255,255,.85);color:var(--white);text-align:center;font-weight:700;font-size:25px;line-height:32px;padding-top:14px}
.stat.plans{left:0;background:var(--charcoal)}
.stat.contacts{left:206px;background:var(--orange)}
.stat.documents{left:411px;background:var(--green)}
.stat.messages{left:619px;background:var(--blue)}
.section-title{position:absolute;left:0;width:801px;text-align:center;font-size:25px;font-weight:600;color:var(--ink)}
.section-title span{border-bottom:1px solid var(--ink);padding-bottom:1px}
.plan-types{position:absolute;top:477px;left:0;width:801px;height:120px}
.plan-type{position:absolute;top:0;width:120px;margin-left:-60px;text-align:center}
.plan-type .ring{width:80px;height:80px;border-radius:50%;border:2px solid #dcdcdc;background:var(--page);margin:0 auto;display:flex;align-items:center;justify-content:center}
.plan-type p{margin-top:7px;font-size:21px;font-weight:700;color:var(--deep)}
.active-plan{position:absolute;left:-1px;width:802px;display:flex;align-items:center}
.active-plan.alt{background:var(--row)}
.badge{width:47px;height:40px;color:var(--white);font-size:13px;display:flex;align-items:center;justify-content:center;flex:none}
.badge.start{background:var(--navy)}
.badge.end{background:var(--orange)}
.plan-body{position:relative;flex:1;height:40px;margin-left:12px;font-size:13px;color:#2b2b2b}
.plan-name{position:absolute;left:0;top:-5px;font-size:16px;color:#444}
.plan-meta{position:absolute;top:22px}
.footer{position:absolute;left:0;top:891px;width:1200px;height:45px;background:var(--navy);color:#e6ecf2;font-size:13px;text-align:center;line-height:45px}
</style>
</head>
<body>
<div class="frame">
  <aside class="sidebar">
    <div class="user">
      <svg width="46" height="46" viewBox="0 0 46 46"><circle cx="23" cy="23" r="21" fill="none" stroke="#fff" stroke-width="3"/><circle cx="23" cy="18" r="7" fill="#fff"/><path d="M10 37c3-8 23-8 26 0" fill="#fff"/></svg>
      <div><p class="user-name">Dana Whitlow</p><p class="user-links">View Account, Logout</p></div>
    </div>
    <ul class="nav">
      <li><svg width="16" height="16" viewBox="0 0 16 16" fill="#243347"><path d="M8 1 1 8h2v6h4v-4h2v4h4V8h2z"/></svg>Home</li>
      <li><svg width="16" height="18" viewBox="0 0 16 18" fill="#243347"><circle cx="4" cy="4" r="3"/><circle cx="12" cy="9" r="3"/><circle cx="4" cy="14" r="3"/></svg>Plans</li>
      <li><svg width="16" height="18" viewBox="0 0 16 18" fill="#243347"><rect x="2" y="1" width="12" height="16" rx="1"/><path d="M5 5h6M5 8h6M5 11h6" stroke="#f47920"/></svg>Documents</li>
      <li><svg width="18" height="14" viewBox="0 0 18 14"><rect x="1" y="1" width="16" height="12" fill="none" stroke="#243347" stroke-width="1.6"/><path d="M1 1l8 7 8-7" fill="none" stroke="#243347" stroke-width="1.6"/></svg>Messages</li>
      <li><svg width="20" height="14" viewBox="0 0 20 14"><rect x="1" y="1" width="18" height="12" fill="#243347"/><circle cx="6" cy="6" r="2" fill="#f47920"/><path d="M11 5h6M11 8h6" stroke="#f47920"/></svg>Contacts</li>
      <li><svg width="16" height="18" viewBox="0 0 16 18" fill="#243347"><path d="M8 1a7 7 0 0 0-4 12.7V17h6v-2h2a1 1 0 0 0 1-1v-2l2-1-2-3A7 7 0 0 0 8 1z"/></svg>Learning</li>
      <li><svg width="20" height="16" viewBox="0 0 20 16" fill="#243347"><circle cx="10" cy="4" r="3"/><circle cx="4" cy="7" r="2.5"/><circle cx="16" cy="7" r="2.5"/><path d="M5 15c0-5 10-5 10 0zM0 15c0-4 5-4 6-3M20 15c0-4-5-4-6-3"/></svg>Community</li>
    </ul>
  </aside>

  <main class="main">
    <div class="brand"><span class="brand-dot"></span><span class="brand-name">Brellomar</span></div>
    <p class="tagline">The most trusted resource for life management</p>
    <div class="account-links">Login<span>|</span>Sign Up</div>

    <div class="banner" role="img" aria-label="Grid of smiling member portrait photos"></div>
    <div class="banner-text">
      <p class="banner-title">Discover Why Brellomar</p>
      <p class="banner-sub">is important to you</p>
    </div>

    <div class="stats">
      <div class="stat plans"><div>4<br>Plans</div></div>
      <div class="stat contacts"><div>12<br>Contacts</div></div>
      <div class="stat documents"><div>8<br>Documents</div></div>
      <div class="stat messages"><div>12<br>Messages</div></div>
    </div>

    <h2 class="section-title" style="top:405px"><span>Recommended Plans</span></h2>

    <div class="plan-types">
      <div class="plan-type" style="left:40px"><div class="ring"><svg width="44" height="30" viewBox="0 0 44 30"><path d="M1 16h12l4-8 5 18 5-24 4 14h12" fill="none" stroke="#0e5ea8" stroke-width="3" stroke-linejoin="round"/></svg></div><p>Life</p></div>
      <div class="plan-type" style="left:179px"><div class="ring"><svg width="44" height="30" viewBox="0 0 44 30" fill="#0e5ea8"><path d="M2 5h26v19H2zM28 10h8l6 7v7H28z"/><circle cx="10" cy="25" r="4"/><circle cx="34" cy="25" r="4"/><path d="M13 9h4v4h4v4h-4v4h-4v-4H9v-4h4z" fill="#fff"/></svg></div><p>Accident</p></div>
      <div class="plan-type" style="left:328px"><div class="ring"><svg width="38" height="36" viewBox="0 0 38 36" fill="#0e5ea8"><path d="M19 2 2 16h5v18h24V16h5z"/><rect x="15" y="22" width="8" height="12" fill="#fff"/><rect x="10" y="17" width="5" height="4" fill="#fff"/><rect x="23" y="17" width="5" height="4" fill="#fff"/></svg></div><p>Home</p></div>
      <div class="plan-type" style="left:472px"><div class="ring"><svg width="44" height="30" viewBox="0 0 44 30" fill="#0e5ea8"><path d="M9 4h26l5 10v12H4V14z"/><path d="M11 7h22l3 7H8z" fill="#fff"/><circle cx="11" cy="19" r="3" fill="#fff"/><circle cx="33" cy="19" r="3" fill="#fff"/><rect x="6" y="24" width="7" height="5"/><rect x="31" y="24" width="7" height="5"/></svg></div><p>Auto</p></div>
      <div class="plan-type" style="left:620px"><div class="ring"><svg width="40" height="40" viewBox="0 0 40 40"><circle cx="20" cy="20" r="17" fill="#0e5ea8"/><ellipse cx="20" cy="20" rx="7" ry="17" fill="none" stroke="#fff" stroke-width="2"/><path d="M3 20h34M6 11h28M6 29h28" stroke="#fff" stroke-width="2"/></svg></div><p>Travel</p></div>
      <div class="plan-type" style="left:760px"><div class="ring"><svg width="34" height="34" viewBox="0 0 34 34" fill="none" stroke="#0e5ea8" stroke-width="3"><path d="M2 10V2h8M24 2h8v8M32 24v8h-8M10 32H2v-8"/><path d="M17 9v16M9 17h16" stroke-width="5"/></svg></div><p>More</p></div>
    </div>

    <h2 class="section-title" style="top:611px"><span>Active Plans</span></h2>

    <div class="active-plan" style="top:682px">
      <div class="badge start">Start</div>
      <div class="plan-body">
        <p class="plan-name">Lorem Ipsum is simply</p>
        <span class="plan-meta" style="left:0">Start: 5/10/2015</span>
        <span class="plan-meta" style="left:234px">End: 5/10/2015</span>
        <span class="plan-meta" style="left:455px">Documents: 0</span>
        <span class="plan-meta" style="right:6px">Contacts: 1</span>
      </div>
    </div>
    <div class="active-plan alt" style="top:743px;height:53px;align-items:flex-start;padding-top:7px">
      <div class="badge end">End</div>
      <div class="plan-body">
        <p class="plan-name">Lorem Ipsum is simply</p>
        <span class="plan-meta" style="left:0">Start: 5/10/2015</span>
        <span class="plan-meta" style="left:234px">End: 5/10/2015</span>
        <span class="plan-meta" style="left:455px">Documents: 0</span>
        <span class="plan-meta" style="right:6px;top:18px">Contacts: 1</span>
      </div>
    </div>
    <div class="active-plan" style="top:815px">
      <div class="badge start">Start</div>
      <div class="plan-body">
        <p class="plan-name">Lorem Ipsum is simply</p>
        <span class="plan-meta" style="left:0">Start: 5/10/2015</span>
        <span class="plan-meta" style="left:234px">End: 5/10/2015</span>
        <span class="plan-meta" style="left:455px">Documents: 0</span>
        <span class="plan-meta" style="right:6px">Contacts: 1</span>
      </div>
    </div>
  </main>

  <footer class="footer">Copyright © 2015 Brellomar. All Rights Reserved.</footer>
</div>
</body>
</html>
```